Moving comapny Postcard mailer Design

I am looking for a 6x9 postcard with real images of our team. I would like to add the same review we currently have , I want the colors of the postcard to be orange and white. I want the team picture to be enlarged with the other pictures to be mimized. I will add example postcards to give rough ideas. My company is called Brandwell Moving and the postcards with that name are our current postcards. The additional postcards are from other companies who have better postcards than mine. My goal is for my postcard to be better that theirs.

Target Market(s)

Wealthy people in the 35+ age group

Industry/Entity Type

Moving company

Requirements
Must have
• Beauty

```html
<!DOCTYPE html>
<html lang="en">
<head>
<meta charset="utf-8">
<title>Brandwell Moving Postcard</title>
<link rel="stylesheet" href="https://fonts.googleapis.com/css2?family=Montserrat:wght@600;700;800;900&family=Arimo:wght@400;700&display=swap">
<style>
:root{
  --orange:#f0592a;
  --orange-deep:#e24d1f;
  --blue:#2b5cb2;
  --blue-deep:#234d99;
  --navy:#1f3d66;
  --ink:#111;
  --white:#fff;
  --tab:#efefef;
  --page:#ffffff;
  --line:#8a8a8a;
  --stamp:#f2f2f2;
}
*{box-sizing:border-box;margin:0;padding:0}
html,body{width:1200px;height:2432px;overflow:hidden;background:var(--page)}
body{position:relative;font-family:"Arimo",Arial,sans-serif;color:var(--ink)}
.card{position:absolute;left:80px;width:1040px;height:693px;background:var(--white);overflow:hidden;box-shadow:0 6px 16px rgba(0,0,0,.22)}
.card--front{top:349px}
.card--back{top:1391px}

/* front */
.front-photo{position:absolute;left:0;top:0;width:1040px;height:625px;
  background:linear-gradient(180deg,#b7c3d8 0%,#8ea5b3 30%,#5c6e56 48%,#2c2f35 62%,#6f7276 80%,#9a9ca0 100%)}
.front-fade{position:absolute;left:0;top:0;width:1040px;height:625px;
  background:linear-gradient(90deg,var(--blue) 0%,var(--blue) 22%,rgba(43,92,178,.85) 38%,rgba(43,92,178,.35) 52%,rgba(43,92,178,0) 62%)}
.logo-tab{position:absolute;left:72px;top:0;width:193px;height:194px;background:var(--tab);border-radius:0 0 40px 40px;
  display:flex;align-items:center;justify-content:center;text-align:center}
.brand-name{font-family:"Montserrat",sans-serif;font-weight:800;color:var(--blue);font-size:24px;line-height:1.1}
.headline{position:absolute;left:52px;top:222px;font-family:"Montserrat",sans-serif;color:var(--white);text-transform:uppercase}
.headline__lead{font-size:44px;font-weight:600;line-height:1}
.headline__big{font-size:88px;font-weight:900;color:var(--orange);line-height:.95;letter-spacing:-1px}
.headline__sub{font-size:38px;font-weight:600;line-height:1.1;margin-top:4px}
.review{position:absolute;left:47px;top:440px;width:386px;height:138px;background:var(--white);border-radius:40px;padding:14px 26px 0 30px}
.review__mark{display:block;width:30px;height:24px}
.review__text{font-size:11.4px;line-height:1.2;margin-top:6px}
.badge{position:absolute;width:160px;height:160px}
.badge svg{position:absolute;inset:0;width:100%;height:100%}
.badge__text{position:absolute;inset:0;display:flex;flex-direction:column;align-items:center;justify-content:center;color:var(--white);text-align:center}
.badge__pct{font-family:"Montserrat",sans-serif;font-weight:700;font-size:48px;line-height:1;letter-spacing:-2px}
.badge__pct small{font-size:17px;font-weight:600;letter-spacing:0}
.badge__label{font-family:"Montserrat",sans-serif;font-weight:800;font-size:15px;margin-top:2px}
.badge__note{font-size:10px;line-height:1.2;margin-top:3px}
.badge--sm{width:134px;height:134px}
.badge--sm .badge__pct{font-size:40px}
.badge--sm .badge__pct small{font-size:14px}
.badge--sm .badge__label{font-size:12px}
.badge--sm .badge__note{font-size:8.5px}
.cta-pill{position:absolute;background:var(--orange);color:var(--white);border-radius:30px;display:flex;align-items:center;justify-content:center;gap:8px;white-space:nowrap}
.cta-pill--front{left:124px;top:611px;width:791px;height:52px;font-size:21px}
.cta-pill strong{font-weight:700;margin-right:8px}
.icon{width:22px;height:22px;flex:none}

/* back */
.back-header{position:absolute;left:0;top:0;width:516px;height:151px;background:linear-gradient(90deg,var(--navy),var(--blue) 70%,#3a6ac0);padding:30px 28px 0 56px;color:var(--white)}
.tagline{font-family:"Montserrat",sans-serif;font-weight:900;font-size:35px;line-height:1;letter-spacing:-.5px}
.tagline span{color:var(--orange)}
.intro{font-size:11.3px;line-height:1.2;margin-top:8px}
.back-photo{position:absolute;left:0;top:151px;width:516px;height:442px;
  background:linear-gradient(180deg,#6f6a64 0%,#8a8276 35%,#5d6c4c 70%,#4e6a3a 100%)}
.back-cta{position:absolute;left:57px;top:605px;font-family:"Arimo",sans-serif;font-weight:700;font-size:24px;color:var(--navy);white-space:nowrap}
.cta-pill--back{left:49px;top:644px;width:420px;height:28px;font-size:19px;gap:4px}
.cta-pill--back .icon{width:18px;height:18px}
.back-brand{position:absolute;left:612px;top:98px;width:140px;text-align:center}
.back-brand .brand-name{font-size:20px}
.stamp-box{position:absolute;left:790px;top:72px;width:138px;height:137px;background:var(--stamp)}
.address-line{position:absolute;left:632px;width:296px;height:1px;background:var(--line)}
</style>
</head>
<body>
<svg width="0" height="0" style="position:absolute" aria-hidden="true">
  <symbol id="seal" viewBox="0 0 160 160">
    <g fill="var(--orange)">
      <circle cx="80" cy="80" r="68"/>
      <circle cx="146" cy="80" r="14"/><circle cx="137.2" cy="113" r="14"/><circle cx="113" cy="137.2" r="14"/>
      <circle cx="80" cy="146" r="14"/><circle cx="47" cy="137.2" r="14"/><circle cx="22.8" cy="113" r="14"/>
      <circle cx="14" cy="80" r="14"/><circle cx="22.8" cy="47" r="14"/><circle cx="47" cy="22.8" r="14"/>
      <circle cx="80" cy="14" r="14"/><circle cx="113" cy="22.8" r="14"/><circle cx="137.2" cy="47" r="14"/>
    </g>
  </symbol>
  <symbol id="phone" viewBox="0 0 24 24">
    <path d="M6.6 3.5l2.6 3.6-1.6 2.1c1.2 2.6 3.1 4.5 5.6 5.7l2.1-1.6 3.6 2.6-1.2 3c-7.3.2-13.3-5.8-13.2-13.2z" fill="none" stroke="#fff" stroke-width="1.6" stroke-linejoin="round"/>
  </symbol>
  <symbol id="globe" viewBox="0 0 24 24">
    <g fill="none" stroke="#fff" stroke-width="1.6"><circle cx="12" cy="12" r="9.5"/><ellipse cx="12" cy="12" rx="4.2" ry="9.5"/><path d="M2.5 12h19M4 7h16M4 17h16"/></g>
  </symbol>
</svg>

<section class="card card--front">
  <div class="front-photo" role="img" aria-label="Photo of the moving crew in black uniforms standing in front of an open box truck, with white trucks and trees around"></div>
  <div class="front-fade"></div>
  <div class="logo-tab"><span class="brand-name">Brandwell<br>Moving</span></div>
  <h1 class="headline">
    <div class="headline__lead">Are you</div>
    <div class="headline__big">Moving?</div>
    <div class="headline__sub">Late us handle<br>the heavy lifting!</div>
  </h1>
  <blockquote class="review">
    <svg class="review__mark" viewBox="0 0 30 24" aria-hidden="true"><path fill="var(--orange)" d="M12 2C5 4 1 9 1 15c0 4 2.5 7 6 7 3 0 5-2 5-5s-2-5-5-5c0-3 2-5.5 6-7zM28 2c-7 2-11 7-11 13 0 4 2.5 7 6 7 3 0 5-2 5-5s-2-5-5-5c0-3 2-5.5 6-7z"/></svg>
    <p class="review__text">This company is incredible! After working all day, they came to our house and without skipping a beat began efficiently moving our heavy household items. They had a great attitude, very friendly, and clearly enjoyed workingwith each other! They took extremely good care of my household items. Thank you for a great experience!</p>
  </blockquote>
  <div class="badge" style="left:486px;top:428px"><svg><use href="#seal"/></svg><div class="badge__text"><div class="badge__pct">25%<small>OFF</small></div><div class="badge__label">MOVES UNDER</div><div class="badge__note">With this card<br>Call for details</div></div></div>
  <div class="badge" style="left:650px;top:426px"><svg><use href="#seal"/></svg><div class="badge__text"><div class="badge__pct">50%<small>OFF</small></div><div class="badge__label">MOVES UNDER</div><div class="badge__note">With this card<br>Call for details</div></div></div>
  <div class="badge" style="left:820px;top:424px"><svg><use href="#seal"/></svg><div class="badge__text"><div class="badge__pct">100%<small>OFF</small></div><div class="badge__label">MOVES UNDER</div><div class="badge__note">With this card<br>Call for details</div></div></div>
  <div class="cta-pill cta-pill--front"><strong>Call us today to get started!</strong><svg class="icon"><use href="#phone"/></svg>(865) 555-0148 <svg class="icon"><use href="#globe"/></svg>www.brandwellmoving.com</div>
</section>

<section class="card card--back">
  <header class="back-header">
    <h2 class="tagline">MOVING.<span>MADE.SIMPLE.</span></h2>
    <p class="intro">For over ten years, our team at Brandwell Moving has been providing Eastern Tennessee with unparalleled custom moving experiences. We prioritize safety, timeliness,and communication to ensure our customers are happy and stress-free before, during, and after their move. No matter where you need to go, we're here to help!</p>
  </header>
  <div class="back-photo" role="img" aria-label="Photo of two movers carrying a plastic-wrapped piece of furniture out of a house garage"></div>
  <div class="badge badge--sm" style="left:53px;top:172px"><svg><use href="#seal"/></svg><div class="badge__text"><div class="badge__pct">25%<small>OFF</small></div><div class="badge__label">MOVES UNDER</div><div class="badge__note">With this card<br>Call for details</div></div></div>
  <div class="badge badge--sm" style="left:55px;top:302px"><svg><use href="#seal"/></svg><div class="badge__text"><div class="badge__pct">50%<small>OFF</small></div><div class="badge__label">MOVES UNDER</div><div class="badge__note">With this card<br>Call for details</div></div></div>
  <div class="badge badge--sm" style="left:47px;top:430px"><svg><use href="#seal"/></svg><div class="badge__text"><div class="badge__pct">100%<small>OFF</small></div><div class="badge__label">MOVES UNDER</div><div class="badge__note">With this card<br>Call for details</div></div></div>
  <p class="back-cta">CALL US TODAY &nbsp;TO GET STARTED!</p>
  <div class="cta-pill cta-pill--back"><svg class="icon"><use href="#phone"/></svg>(865) 555-0148<svg class="icon"><use href="#globe"/></svg>www.brandwellmoving.com</div>
  <div class="back-brand"><span class="brand-name">Brandwell<br>Moving</span></div>
  <div class="stamp-box"></div>
  <div class="address-line" style="top:299px"></div>
  <div class="address-line" style="top:371px"></div>
  <div class="address-line" style="top:445px"></div>
</section>
</body>
</html>
```